Velmira Body Oil Label for 4 -8 oz bottles

We are selling 4 and 8 oz body oils and need a label to put on our bottles. I'm not sure if we want a label for the front and also the back of the bottle or just one label in the front. You can give me examples of each way. Attached is our logo on a blue background but the background will change colors depending on the scent as specified in the design description. Our bottle will be either clear or white with a pump spray type lid as shown in the attached example. Attached are also our design criteria which is needed for the labels.
Updates

We have decided to use the disc top cap and not the pump spray cap. If you are able to, please show us the design on the 4 oz bottle with the disc top cap. Thanks

Target Market(s)

women

Industry/Entity Type

skincare, cosmetics

Font styles to use
Serif
Sans Serif

Requirements
Must have
• stylish name for each scented oil which contrasts the font in the logo. Also must have darker colors since the logo colors are lighter.
Nice to have
• Border around the labels, maybe one solid color or maybe two complimenting colors which go well with the fragrnace name
Should not have
• background colors that match the logo colors

```html
<!DOCTYPE html>
<html lang="en">
<head>
<meta charset="utf-8">
<title>Velmira Body Oils – Cotton Candy Labels</title>
<link href="https://fonts.googleapis.com/css2?family=Outfit:wght@400;500;600&family=Lilita+One&family=Cormorant+Garamond:ital,wght@1,500&display=swap" rel="stylesheet">
<style>
  :root {
    --bg-teal: #5bb7c6;
    --sky: #98dbe5;
    --pink: #f4b3c6;
    --pink-soft: #f8ccd9;
    --pink-deep: #ef8fa9;
    --white: #ffffff;
    --ink: #2a2a2a;
    --heading-blue: #7fd0de;
    --warn-red: #e8344a;
    --badge-navy: #1f3a7a;
  }
  * { margin: 0; padding: 0; box-sizing: border-box; }
  html, body { width: 1200px; height: 855px; overflow: hidden; }
  body {
    background: var(--bg-teal);
    font-family: "Outfit", sans-serif;
    color: var(--ink);
    position: relative;
  }
  .label {
    position: absolute;
    top: 45px;
    width: 256px;
    height: 765px;
    overflow: hidden;
    box-shadow: 0 8px 24px rgba(0,0,0,0.12);
  }
  .label--back { left: 329px; background: linear-gradient(180deg, #f2fafc 0%, #ffffff 45%, #fdf3f6 80%); }
  .label--front { left: 615px; background: var(--pink); }

  .section-title {
    position: absolute; left: 0; right: 0; text-align: center;
    font-family: "Lilita One", sans-serif;
    font-size: 13.5px; line-height: 16px; letter-spacing: 0.3px;
    color: var(--heading-blue);
  }
  .section-body {
    position: absolute; left: 8px; right: 8px; text-align: center;
    font-size: 10.8px; line-height: 13.3px; white-space: nowrap;
  }
  .title-ingredients { top: 94px; }
  .body-ingredients { top: 114px; }
  .title-directions { top: 249px; }
  .body-directions { top: 269px; line-height: 12.6px; }
  .title-warnings { top: 360px; color: var(--pink-deep); display: flex; justify-content: center; align-items: center; gap: 6px; }
  .warn-dot {
    width: 13px; height: 13px; border-radius: 50%;
    background: var(--warn-red); color: var(--white);
    font-family: "Outfit", sans-serif; font-size: 9px; font-weight: 600;
    display: inline-flex; align-items: center; justify-content: center;
  }
  .warning-list { position: absolute; top: 382px; left: 0; right: 0; list-style: none; text-align: center; font-size: 10.6px; line-height: 16px; white-space: nowrap; }
  .warning-list li::before { content: "✕"; color: var(--warn-red); font-weight: 600; margin-right: 9px; }
  .warning-list li.continued::before { content: none; }

  .origin-badge {
    position: absolute; left: 89px; top: 563px;
    width: 78px; height: 78px; border-radius: 50%;
    background: var(--white); border: 5px solid var(--badge-navy);
    z-index: 2;
  }
  .back-wave { position: absolute; left: 0; top: 620px; width: 256px; }
  .distributor {
    position: absolute; left: 0; right: 0; top: 666px;
    text-align: center; color: var(--white);
    font-size: 13px; font-weight: 500; line-height: 19.5px;
  }

  .front-top { position: absolute; left: 0; top: 0; width: 256px; height: 280px; }
  .brand {
    position: absolute; left: 0; right: 0; top: 100px; text-align: center;
    color: var(--white);
  }
  .brand-name { font-family: "Cormorant Garamond", serif; font-style: italic; font-weight: 500; font-size: 46px; line-height: 48px; }
  .brand-sub { font-family: "Outfit", sans-serif; font-size: 9px; letter-spacing: 3px; margin-top: 2px; padding-left: 60px; }
  .cloud-area { position: absolute; background: var(--pink-soft); }
  .cloud-area--upper { left: 0; top: 262px; width: 110px; height: 40px; }
  .cloud-area--lower { left: 166px; top: 442px; width: 90px; height: 62px; }
  .scent-name {
    position: absolute; left: 0; right: 0; top: 340px; text-align: center;
    font-family: "Lilita One", sans-serif; color: var(--white);
    font-size: 52px; line-height: 46px; letter-spacing: 0.5px;
  }
  .scent-name span { display: block; }
  .scent-name span + span { padding-left: 8px; }
  .features { position: absolute; left: 0; right: 0; top: 528px; list-style: none; color: var(--white); font-size: 15.5px; }
  .features li { display: flex; align-items: center; justify-content: center; gap: 8px; height: 33px; }
  .feature-icon { width: 16px; height: 16px; }
  .net-weight {
    position: absolute; left: 45px; top: 694px; width: 166px; height: 27px;
    background: var(--white); border-radius: 14px;
    text-align: center; font-size: 12px; line-height: 27px;
  }
</style>
</head>
<body>

<section class="label label--back" aria-label="Back label">
  <h2 class="section-title title-ingredients">INGREDIENTS</h2>
  <p class="section-body body-ingredients">Cocos Nucifera (Coconut) Oil, Prunus<br>Amygdalus Dulcis (Almond) Oil, Vitis<br>Vinifera (Grapeseed) Oil, Sesamum<br>Indicum (Sesame) Seed Oil, Simmondsia<br>Chinensis (Jojoba) Oil, Tocopheryl Acetate<br>(Vitamin E). Essential oils, and fragrances.</p>

  <h2 class="section-title title-directions">DIRECTIONS</h2>
  <p class="section-body body-directions">Apply a small amount to skin and<br>massage until absorbed. Use daily for<br>best results.</p>

  <h2 class="section-title title-warnings"><span class="warn-dot">!</span>WARNINGS / DISCLAIMERS</h2>
  <ul class="warning-list">
    <li>For external use only.</li>
    <li>Avoid contact with eyes.</li>
    <li>Discontinue use if irritation occurs.</li>
    <li>Keep out of reach of children.</li>
    <li>Contains nut oils — use with caution</li>
    <li class="continued">if you have nut allergies.</li>
  </ul>

  <div class="origin-badge" role="img" aria-label="Origin certification badge"></div>

  <svg class="back-wave" width="256" height="145" viewBox="0 0 256 145" aria-hidden="true">
    <path d="M0 14 Q16 4 32 14 T64 14 T96 14 T128 14 T160 14 T192 14 T224 14 T256 14 V145 H0 Z" fill="#f6b7c9"/>
    <path d="M0 18 Q16 8 32 18 T64 18 T96 18 T128 18 T160 18 T192 18 T224 18 T256 18 V145 H0 Z" fill="#98dbe5"/>
  </svg>
  <p class="distributor">Distributed by Velmira<br>2270 Larkspur Lane<br>Fort Collins, CO 80524</p>
</section>

<section class="label label--front" aria-label="Front label">
  <svg class="front-top" width="256" height="280" viewBox="0 0 256 280" aria-hidden="true">
    <path d="M0 0 H256 V250 Q240 236 222 248 T186 250 T150 252 T114 250 T78 254 T42 246 T0 256 Z" fill="#98dbe5"/>
    <path d="M0 256 Q21 246 42 246 T78 254 T114 250 T150 252 T186 250 T222 248 Q240 236 256 250" fill="none" stroke="#ffffff" stroke-width="3"/>
  </svg>
  <div class="brand">
    <div class="brand-name">Velmira</div>
    <div class="brand-sub">BODY OILS</div>
  </div>
  <div class="cloud-area cloud-area--upper" role="img" aria-label="Pastel cloud illustration"></div>
  <div class="cloud-area cloud-area--lower" role="img" aria-label="Pastel cloud illustration"></div>

  <h1 class="scent-name"><span>COTTON</span><span>CANDY</span></h1>

  <ul class="features">
    <li><svg class="feature-icon" viewBox="0 0 16 16" aria-hidden="true"><circle cx="8" cy="8" r="6.5" fill="none" stroke="#fff" stroke-width="1.5"/><path d="M4 12 L12 4" stroke="#fff" stroke-width="1.5"/></svg>Non - Greesy</li>
    <li><svg class="feature-icon" viewBox="0 0 16 16" aria-hidden="true"><path d="M8 1 C5 6 3 8 3 10.5 A5 5 0 0 0 13 10.5 C13 8 11 6 8 1 Z" fill="#fff"/></svg>Ultra Moisturizing</li>
    <li><svg class="feature-icon" viewBox="0 0 16 16" aria-hidden="true"><path d="M6 2 C3.5 6 2 7.5 2 9.5 A4 4 0 0 0 10 9.5 C10 7.5 8.5 6 6 2 Z" fill="#fff"/><circle cx="11.5" cy="11.5" r="3.5" fill="#fff"/></svg>With Vitamin E</li>
  </ul>

  <div class="net-weight">Net Wt. 4 fl. oz. (118 mL)</div>
</section>

</body>
</html>
```